Rioja winery needs a new label design

A family-owned winery in Spain's Rioja Oriental region is looking to create a new label for a wine named "Dorvi" Arabic for Castle, that reflects the land from which the wine is born. From the remote village of Almeda, La Rioja Oriental, with the backdrop of the Sierra Yerga mountains and the Barrio de Bodegas, or group of caves where locals have produced wines for centuries. Wine name:
2018 Dorvi Rioja Tempranillo
Almeda, Rioja Oriental
Spain

Font styles to use
Serif
Sans Serif
Decorative
Script

Requirements
Must have
• vines, vineyards, grapes
Nice to have
• mountains,
Should not have
• castles. we already have a label design with the castle

```html
<!DOCTYPE html>
<html lang="en">
<head>
<meta charset="utf-8">
<title>Dorvi Rioja Tempranillo 2018 – Label</title>
<link rel="stylesheet" href="https://fonts.googleapis.com/css2?family=Allura&family=Montserrat:wght@400;500&display=swap">
<style>
  :root {
    --backdrop: #15243a;
    --label-paper: #fbfbfa;
    --gold: #d9a021;
    --gold-deep: #c9801a;
    --gold-light: #f2c14a;
    --sketch-grey: #e2e4e9;
    --sketch-grey-soft: #eff0f3;
    --band-text: #fff6e0;
  }
  html, body {
    margin: 0;
    padding: 0;
    width: 1200px;
    height: 860px;
    overflow: hidden;
    background: var(--backdrop);
  }
  .canvas {
    position: relative;
    width: 1200px;
    height: 860px;
    display: flex;
    align-items: center;
    justify-content: center;
  }
  .label {
    position: relative;
    width: 940px;
    height: 620px;
    background: var(--label-paper);
    overflow: hidden;
    box-shadow: 0 20px 50px rgba(0,0,0,0.35);
  }
  .landscape-illustration {
    position: absolute;
    left: 560px;
    top: 250px;
    width: 380px;
    height: 370px;
    border-radius: 6px 0 0 0;
    background: linear-gradient(180deg, var(--sketch-grey-soft) 0%, var(--sketch-grey) 100%);
  }
  .wine-name {
    position: absolute;
    left: 110px;
    top: 40px;
    margin: 0;
    font-family: "Allura", cursive;
    font-weight: 400;
    font-size: 270px;
    line-height: 1;
    color: var(--gold);
  }
  .varietal {
    position: absolute;
    left: 330px;
    top: 350px;
    width: 440px;
  }
  .varietal-rule {
    height: 1.5px;
    background: var(--gold);
  }
  .varietal-rule.top {
    margin-left: 70px;
  }
  .varietal-rule.bottom {
    margin-right: 40px;
  }
  .varietal-name {
    margin: 12px 0;
    text-align: center;
    font-family: "Montserrat", sans-serif;
    font-weight: 400;
    font-size: 24px;
    letter-spacing: 0.18em;
    color: var(--gold-deep);
  }
  .vintage {
    position: absolute;
    left: 560px;
    top: 440px;
    width: 200px;
    margin: 0;
    text-align: center;
    font-family: "Montserrat", sans-serif;
    font-weight: 400;
    font-size: 40px;
    letter-spacing: 0.04em;
    color: var(--gold-deep);
  }
  .origin-band {
    position: absolute;
    right: 0;
    bottom: 0;
    width: 470px;
    height: 140px;
  }
  .origin-text {
    position: absolute;
    right: 40px;
    bottom: 24px;
    margin: 0;
    text-align: center;
    font-family: "Montserrat", sans-serif;
    font-weight: 400;
    font-size: 18px;
    line-height: 1.35;
    color: var(--band-text);
  }
</style>
</head>
<body>
  <main class="canvas">
    <section class="label">
      <div class="landscape-illustration" role="img" aria-label="Fine line illustration of the Sierra Yerga mountains above rows of vineyard vines with grape clusters and the hillside wine caves"></div>

      <h1 class="wine-name">Dorvi</h1>

      <div class="varietal">
        <div class="varietal-rule top"></div>
        <p class="varietal-name">RIOJA TEMPRANILLO</p>
        <div class="varietal-rule bottom"></div>
      </div>

      <p class="vintage">2018</p>

      <svg class="origin-band" viewBox="0 0 470 140" preserveAspectRatio="none" aria-hidden="true">
        <defs>
          <linearGradient id="band-gold" x1="0" y1="1" x2="1" y2="0">
            <stop offset="0" stop-color="#c9801a"/>
            <stop offset="0.6" stop-color="#e3a82a"/>
            <stop offset="1" stop-color="#f2c14a"/>
          </linearGradient>
        </defs>
        <path d="M0 140 C20 90 40 60 90 62 C150 64 170 40 240 36 C310 32 360 20 470 10 L470 140 Z" fill="url(#band-gold)"/>
      </svg>
      <p class="origin-text">Almeda, Rioja Oriental<br>Spain</p>
    </section>
  </main>
</body>
</html>
```